Criação de Kit Layout de Posts para Redes Sociais (Facebook, Instagram e etc) para Esportes
" Ofereço serviços de personal trainer para alunos em academias, condomínios, parques, etc.; serviços de personal trainer on-line ao vivo; e serviços de consultoria para prescrição de treinos (sem o acompanhamento durante a execução em si dos treinos) "

```html
<!DOCTYPE html>
<html lang="pt-BR">
<head>
<meta charset="UTF-8">
<title>Rafael Moreira Personal Trainer – Atravesse Barreiras</title>
<link rel="stylesheet" href="https://fonts.googleapis.com/css2?family=Montserrat:ital,wght@0,600;0,700;0,800;1,800;1,900&display=swap">
<style>
  :root {
    --green: #2fe03a;
    --green-dark: #1aa82a;
    --ink: #111412;
    --night: #1c2120;
    --white: #ffffff;
    --panel: #f3f4f2;
  }
  * { margin: 0; padding: 0; box-sizing: border-box; }
  html, body { width: 1200px; height: 1200px; overflow: hidden; background: var(--ink); }
  .post {
    position: relative; width: 1200px; height: 1200px; overflow: hidden;
    font-family: "Montserrat", sans-serif; color: var(--white);
  }
  .gym-photo {
    position: absolute; inset: 0;
    background:
      radial-gradient(ellipse at 78% 55%, #a88a82 0%, rgba(120,100,95,0.4) 25%, transparent 50%),
      radial-gradient(ellipse at 45% 25%, #c9c2bb 0%, rgba(150,145,140,0.5) 30%, transparent 60%),
      linear-gradient(180deg, #8e9090 0%, #4c5253 45%, #2b3030 75%, #1d2121 100%);
  }
  .shade-left {
    position: absolute; inset: 0;
    background: linear-gradient(90deg, rgba(17,20,18,0.92) 0%, rgba(17,20,18,0.7) 35%, rgba(17,20,18,0) 65%);
  }
  .decor { position: absolute; inset: 0; }
  .band { position: absolute; left: 0; width: 1200px; background: var(--ink); }
  .band--top { top: 0; height: 50px; }
  .band--bottom { bottom: 0; height: 34px; }

  .brand {
    position: absolute; left: 0; top: 48px; width: 580px; height: 192px;
  }
  .brand-name {
    position: absolute; left: 84px; top: 112px;
    display: flex; align-items: center; gap: 14px;
    font-weight: 800; font-size: 38px; line-height: 1; color: var(--ink); letter-spacing: 1px;
  }
  .brand-mark { width: 28px; height: 28px; background: var(--green); flex: none; }
  .brand-role {
    position: absolute; left: 126px; top: 174px;
    font-weight: 800; font-size: 25px; line-height: 1; color: var(--green-dark); letter-spacing: 3px;
  }

  .headline {
    position: absolute; left: 46px; top: 430px;
    font-weight: 900; font-style: italic; font-size: 98px; line-height: 1.02;
    text-transform: uppercase; letter-spacing: 1px;
    text-shadow: 0 4px 14px rgba(0,0,0,0.5);
  }
  .subhead {
    position: absolute; left: 46px; top: 748px;
    font-weight: 900; font-style: italic; font-size: 54px; text-transform: uppercase;
  }
  .support {
    position: absolute; left: 46px; top: 828px;
    font-weight: 800; font-style: italic; font-size: 35px; line-height: 1.1; color: var(--green);
  }
  .cta {
    position: absolute; left: 0; top: 976px; width: 510px; height: 70px;
    background: var(--panel);
    clip-path: polygon(0 0, 100% 0, 94% 100%, 0 100%);
    display: flex; align-items: center; padding-left: 48px;
    font-weight: 900; font-style: italic; font-size: 32px; color: var(--ink);
  }
  .contacts {
    position: absolute; left: 40px; top: 1054px; list-style: none;
  }
  .contacts li {
    display: flex; align-items: center; gap: 14px; height: 34px;
    font-weight: 700; font-size: 26px; line-height: 1;
  }
  .contacts svg { width: 24px; height: 24px; flex: none; }
</style>
</head>
<body>
<main class="post">
  <div class="gym-photo" role="img" aria-label="Foto de academia com mulher fazendo agachamento com barra e outra aluna treinando em máquina ao fundo"></div>
  <div class="shade-left"></div>

  <svg class="decor" viewBox="0 0 1200 1200" aria-hidden="true">
    <g stroke="var(--green)" stroke-width="3" opacity="0.8">
      <line x1="560" y1="1200" x2="1200" y2="420"/>
      <line x1="720" y1="1200" x2="1200" y2="620"/>
      <line x1="0" y1="1000" x2="420" y2="480"/>
    </g>
    <polygon points="1060,1080 1200,900 1200,1166 1020,1166" fill="var(--green)" opacity="0.85"/>
  </svg>

  <svg class="band band--top" viewBox="0 0 1200 50" preserveAspectRatio="none" aria-hidden="true">
    <rect width="1200" height="50" fill="var(--ink)"/>
    <g fill="var(--green)">
      <polygon points="560,10 640,10 625,40 545,40"/>
      <polygon points="680,10 760,10 745,40 665,40"/>
      <polygon points="800,10 880,10 865,40 785,40"/>
      <polygon points="920,10 1000,10 985,40 905,40"/>
      <polygon points="1040,10 1120,10 1105,40 1025,40"/>
      <polygon points="1160,10 1200,10 1200,40 1145,40"/>
    </g>
  </svg>

  <svg class="brand" viewBox="0 0 580 192" aria-hidden="true">
    <polygon points="0,0 580,0 470,192 0,192" fill="var(--green)"/>
    <polygon points="0,10 552,10 450,182 0,182" fill="var(--white)"/>
  </svg>
  <div class="brand-name"><span class="brand-mark"></span>RAFAEL MOREIRA</div>
  <div class="brand-role">PERSONAL TRAINER</div>

  <h1 class="headline">Atravesse<br>Barreiras</h1>
  <p class="subhead">Faça correto!</p>
  <p class="support">Todo apoio correto para manter<br>seus treinos saudáveis</p>

  <div class="cta">ENTRE EM CONTATO</div>
  <ul class="contacts">
    <li>
      <svg viewBox="0 0 24 24"><circle cx="12" cy="12" r="10.5" fill="none" stroke="#fff" stroke-width="2"/><path d="M8.5 7.5l2 2-1 1.5a7 7 0 0 0 3.5 3.5l1.5-1 2 2-1.5 1.5c-4 0-8-4-8-8z" fill="#fff"/></svg>
      11 98765-4321
    </li>
    <li>
      <svg viewBox="0 0 24 24"><circle cx="12" cy="12" r="10" fill="#fff"/></svg>
      @personal_rafaelmoreira
    </li>
    <li>
      <svg viewBox="0 0 24 24"><rect x="2" y="5" width="20" height="14" rx="2" fill="#fff"/><path d="M3 6l9 7 9-7" fill="none" stroke="var(--ink)" stroke-width="2"/></svg>
      personal.rafael@mailbox.com
    </li>
  </ul>

  <svg class="band band--bottom" viewBox="0 0 1200 34" preserveAspectRatio="none" aria-hidden="true">
    <rect width="1200" height="34" fill="var(--ink)"/>
    <g fill="var(--green)">
      <polygon points="0,7 60,7 48,27 0,27"/>
      <polygon points="100,7 180,7 168,27 88,27"/>
      <polygon points="220,7 300,7 288,27 208,27"/>
      <polygon points="340,7 420,7 408,27 328,27"/>
      <polygon points="460,7 540,7 528,27 448,27"/>
      <polygon points="580,7 660,7 648,27 568,27"/>
    </g>
  </svg>
</main>
</body>
</html>
```